Design for 3.31” x 84” vinyl banner for tradeshow

Hello, I am looking for a design that will be printed on a 33.31” x 84” vinyl banner for my company’s tradeshow booth.

-Design

My vision: I want to give you the full background, because I think it’ll help. We design insulation for electronic tools that go in high temperature oilwells. Interestingly, a lot of the electronic tools that go down these oil wells are also used in geothermal wells. However the electronics would melt in these high temperature geothermal wells if they were not insulated. A lot of companies that make tools for the oil market are trying to re-purpose their existing tools for the geothermal market…..and to do this, they would need our insulation.

So, our sign needs to conveys this message: Trying to enter the geothermal logging market? it's as simple as increasing the temp. rating for your existing tools

This sign will be placed at our company’s booth at an industry tradeshow. The sign needs to have a similar style to our existing signs. I’ve included images of our booth and all of our other signs. This sign doesn’t have to be identical in artistic style, but be fairly similar.

-Art Requirements:

At least 1 Image of RDP logo

I’ve included several different variations. Use your judgement to select the one that you think is most fitting.

Do not use the portion of the logo that says “40 years”. Feel free to crop that out if you would like.

At least 2 images of logging tools. You can select more than 2 if you think that’s necessary. Logging tools are the long metal tubes.

I’ve included several pictures of different logging tools. I would like to see at least 2 pictures of tools on the banner. Please include the image titled “Full, double centarlizer” It could look cool if this picture extended the full length of the banner (just a suggestion). I purchased these images off of picvault.For the second image of the tool, feel free to include whatever tool you think looks best.

-Colors and font: Like I mentioned above, I would like it to look close to the other signs we have at our booth. Please select colors and fonts that will fit with our other signs.

-Other thoughts/suggestions

When most people in our industry think of geothermal, the automatically associate it with extremely high temperatures. I’m open to seeing warmer colors (orange/red) that help convey this idea.

I’m also open to seeing pictures of geothermal power plants, I included an image of this titled “geothermal” that you may use if you like. This is not mandatory, just a suggestion.

-Text: the main text needs to be: “Trying to enter the Geothermal logging market? Ask us about increasing the temperature rating for your existing tools” No other text is required.

Printing/Art specifications:

I’ll be giving the design I receive off art-hive to a local banner printing shop. I’ve included their printing and art guidelines, please take a look at it and let me know if you have any questions. It’s pretty detailed so I hope it provides you with enough information. The design would have to follow the requirements in the two attached word documents.

Target Market(s)

oil and gas professionals

Industry/Entity Type

oil and gas/geothermal

Font styles to use
Other font styles liked:
• Fonts similar the font used on our other tradeshow signs (images attached)

Colors
F0912C
F2A743
F7CA91
FBE8D2
FDF5EE

Requirements
Must have
• -At least 1 Image of RDP logo, At least 2 images of logging tools (1 of these 2 pictures must be image titled "full double centralizer", he main text needs to be: “Trying to enter the Geothermal logging market? Ask us about increasing the temperature rating for your existing tools” , the design must follow the requirements in the printing and art guideline documents I attached.
Nice to have
• please select colors and fonts that will fit with our other signs.

```html
<!DOCTYPE html>
<html lang="en">
<head>
<meta charset="utf-8">
<title>Redpoint Downhole – Geothermal Logging Banner</title>
<link rel="stylesheet" href="https://fonts.googleapis.com/css2?family=Anton&family=Poppins:wght@500;700;800&display=swap">
<style>
  :root {
    --orange: #ec6f21;
    --ink: #231f20;
    --white: #ffffff;
    --page: #d6d7d7;
    --steel-light: #d9dcdd;
    --steel-mid: #9ea3a6;
    --steel-dark: #5f6468;
    --copper: #c47a3c;
  }
  * { margin: 0; padding: 0; box-sizing: border-box; }
  html, body { width: 1200px; height: 1200px; overflow: hidden; }
  body {
    background: var(--page);
    position: relative;
    font-family: "Poppins", sans-serif;
  }
  .banner {
    position: absolute;
    left: 383px; top: 84px;
    width: 393px; height: 975px;
    background: var(--white);
    overflow: hidden;
  }
  .brand {
    position: absolute;
    left: 88px; top: 30px;
    display: flex; align-items: center; gap: 12px;
  }
  .brand-mark {
    width: 70px; height: 70px;
    background: var(--ink);
    border-radius: 4px;
  }
  .brand-name {
    font-weight: 800;
    font-size: 17px;
    line-height: 1.2;
    color: var(--ink);
  }
  .eyebrow {
    position: absolute;
    left: 27px; top: 124px;
    width: 340px; height: 35px;
    background: var(--orange);
    border-radius: 18px;
    color: var(--white);
    font-weight: 800;
    font-size: 21px;
    line-height: 36px;
    text-align: center;
    white-space: nowrap;
  }
  .eyebrow::after {
    content: "";
    position: absolute;
    left: 163px; bottom: -7px;
    border-left: 7px solid transparent;
    border-right: 7px solid transparent;
    border-top: 8px solid var(--orange);
  }
  .headline {
    font-family: "Anton", sans-serif;
    font-weight: 400;
    color: var(--ink);
  }
  .headline .line {
    position: absolute;
    left: 0; width: 393px;
    text-align: center;
    white-space: nowrap;
    line-height: 1;
  }
  .headline .line-1 { top: 160px; font-size: 64px; letter-spacing: -0.5px; }
  .headline .line-2 { top: 231px; font-size: 43px; }
  .headline .accent { color: var(--orange); }
  .swoosh {
    position: absolute;
    left: 0; top: 640px;
    width: 393px; height: 335px;
  }
  .tool { position: absolute; border-radius: 3px; }
  .tool-caliper {
    left: 76px; top: 303px; width: 30px; height: 519px;
    background: linear-gradient(180deg, var(--steel-mid), var(--steel-light) 45%, var(--steel-dark));
  }
  .tool-rod {
    left: 148px; top: 303px; width: 9px; height: 519px;
    background: linear-gradient(180deg, var(--steel-mid), var(--steel-light) 50%, var(--steel-mid));
  }
  .tool-centralizer {
    left: 169px; top: 300px; width: 204px; height: 489px;
    background: linear-gradient(180deg, var(--copper), var(--steel-light) 25%, var(--steel-mid) 55%, var(--copper) 85%, #f1f1ee);
    border-radius: 8px;
  }
  .ask {
    position: absolute;
    left: 27px; top: 856px;
    width: 340px;
    display: flex; align-items: center; gap: 12px;
    color: var(--white);
    font-weight: 800;
    font-size: 20px;
    white-space: nowrap;
  }
  .ask .rule { flex: 1; height: 2px; background: var(--white); }
  .pitch {
    position: absolute;
    left: 0; top: 886px;
    width: 393px;
    text-align: center;
    color: var(--ink);
    font-weight: 700;
    font-size: 15.5px;
    line-height: 1.25;
    white-space: nowrap;
  }
  .web {
    position: absolute;
    left: 27px; top: 927px;
    width: 340px; height: 32px;
    background: var(--ink);
    border-radius: 16px;
    color: var(--white);
    font-weight: 500;
    font-size: 15px;
    line-height: 32px;
    text-align: center;
    white-space: nowrap;
  }
  .web strong { color: var(--orange); font-weight: 700; }
</style>
</head>
<body>
  <main class="banner">
    <header class="brand">
      <span class="brand-mark"></span>
      <span class="brand-name">REDPOINT<br>DOWNHOLE<br>Inc.</span>
    </header>

    <p class="eyebrow">TRYING TO ENTER THE</p>

    <h1 class="headline">
      <span class="line line-1">GEOTHERMAL</span>
      <span class="line line-2"><span class="accent">LOGGING</span> MARKET?</span>
    </h1>

    <svg class="swoosh" viewBox="0 0 393 335" preserveAspectRatio="none" aria-hidden="true">
      <path d="M0 80 C110 30 250 12 393 18 L393 50 C250 48 120 62 0 104 Z" fill="var(--ink)"/>
      <path d="M0 104 C120 62 250 48 393 50 L393 335 L0 335 Z" fill="var(--orange)"/>
    </svg>

    <div class="tool tool-caliper" role="img" aria-label="Photo of a logging tool with a folding caliper arm assembly"></div>
    <div class="tool tool-rod" role="img" aria-label="Photo of a slim logging rod with two small centralizers"></div>
    <div class="tool tool-centralizer" role="img" aria-label="Photo of a full double centralizer logging tool with copper fittings"></div>

    <p class="ask"><span class="rule"></span>ASK US ABOUT<span class="rule"></span></p>
    <p class="pitch">INCREASING THE TEMPERATURE<br>RATING FOR YOUR EXISTING TOOLS</p>
    <p class="web">www.<strong>redpointdownhole</strong>.com</p>
  </main>
</body>
</html>
```